I need a business card design for a new dance business. I offer classical Indian dance tuition and also professional performances. I want to offer the community a variety of Indian dance experiences which include: group class and private tuition, school and preschool educational courses and workshops. dance theatre performances, community function workshops and performances, Kids Bollywood parties, wedding & conference performances, mouth percussion classes, Indian mythology/ dance costume and make up workshops.
The final design should communicate a feeling and impression of the vibrance and energy of Indian dance.
Updates
Hi Everyone,
Project Deadline Extended
Reason: I would like to refine a few changes to the details of this lovely design and we have run out of time!
Project Deadline Extended
Reason: Still waiting to hear back form designer re two possible changes to the card design. Tomorrow is the deadline and I have sent several messages but with no response. I need to see this through before selecting this lovely design.
Thank you.
Tessa
Industry/Entity Type
Preschool
Requirements
Must have
- The front of the business card should have the photo of me (my face and torso), surrounded entirely by a border of bright magenta (to match the magenta of my lipstick - it is the same as the magenta on my skirt in the second photo). Within the top border I want (perhaps yellow-gold) writing to say "Tessa Marlowe - Artistic Director" and within the bottom border it should read "Copper Lantern Indian Dance." If you turn the card on its side the left border should have my telephone number: 0417 862 049 and the right-hand border should read: copperlanternindiandance@velmora.com
The reverse of the card should be the orange of the dance costume
and I'd like the picture of my feet and legs to be on the right side of the back of the card as a side border. Centre-aligned on the orange background it should read (perhaps in dark magenta):
Indian dance classes + private tuition
School + preschool educational courses and workshops
Dance theatre performances
Community function workshops and performances
Children's Bollywood parties
Wedding + conference performances
Mouth percussion classes
Indian mythology and dance demonstration workshops
Dance costume and make-up workshops
Nice to have
- A lovely artistic but easy-to-read font would be nice.

```html
<!DOCTYPE html>
<html lang="en">
<head>
<meta charset="utf-8">
<title>Copper Lantern Indian Dance – Business Card</title>
<link href="https://fonts.googleapis.com/css2?family=Great+Vibes&family=Cormorant+Garamond:ital,wght@1,600&family=Crimson+Text&display=swap" rel="stylesheet">
<style>
  :root {
    --stage: #3a0606;
    --gold: #ffe100;
    --amber: #ffb300;
    --orange: #f58a00;
    --magenta: #8a1468;
    --plum: #5c0f3c;
    --maroon: #6a0d26;
    --silk: #a0186a;
    --white: #ffffff;
    --bullet: #d40000;
  }
  * { margin: 0; padding: 0; box-sizing: border-box; }
  html, body { width: 1200px; height: 900px; overflow: hidden; }
  body { background: var(--stage); position: relative; }

  .card {
    position: absolute;
    overflow: hidden;
    box-shadow: 0 6px 18px rgba(0,0,0,.55);
  }
  .card--front { left: 104px; top: 110px; width: 440px; height: 674px; }
  .card--back  { left: 646px; top: 114px; width: 438px; height: 670px; }

  /* each face is laid out landscape, then turned to read bottom-to-top */
  .face {
    position: absolute;
    left: 0;
    transform-origin: top left;
    transform: rotate(-90deg);
  }
  .card--front .face { top: 674px; width: 674px; height: 440px;
    background: linear-gradient(to bottom, var(--amber) 0%, var(--gold) 45%, var(--orange) 100%); }
  .card--back .face { top: 670px; width: 670px; height: 438px;
    background: linear-gradient(to bottom, var(--gold) 0%, var(--amber) 40%, var(--orange) 100%); }

  .dancer-photo {
    position: absolute;
    background: radial-gradient(ellipse at 45% 50%, var(--silk) 0%, var(--magenta) 50%, var(--plum) 100%);
  }
  /* front: dancer fills the middle band and the lower-left block, leaving room for the name */
  .card--front .dancer-photo {
    left: 0; top: 124px; width: 674px; height: 256px;
    clip-path: polygon(0 0, 100% 0, 100% 62%, 43% 62%, 43% 100%, 0 100%);
  }
  /* back: full-length dancer along the left edge of the card */
  .card--back .dancer-photo {
    left: 14px; top: 8px; width: 642px; height: 186px;
    border-radius: 93px;
    box-shadow: 0 0 0 6px rgba(255,255,255,.7);
  }

  .brand {
    position: absolute; left: 14px; top: 14px;
    font-family: "Great Vibes", cursive; font-weight: 400;
    font-size: 46px; line-height: 50px;
    color: var(--magenta);
  }
  .brand span { display: block; }
  .brand span + span { padding-left: 70px; }

  .credentials {
    position: absolute; left: 300px; top: 294px;
    font-family: "Cormorant Garamond", serif; font-style: italic; font-weight: 600;
    color: var(--magenta); font-size: 21px; line-height: 26px;
  }
  .credentials .name { font-size: 23px; }

  .contact-band {
    position: absolute; left: 0; bottom: 0; width: 100%; height: 54px;
    background: var(--maroon);
    display: flex; align-items: center; gap: 28px; padding-left: 16px;
    font-family: "Cormorant Garamond", serif; font-style: italic; font-weight: 600;
    font-size: 20px; color: var(--white);
  }

  .services {
    position: absolute; left: 14px; top: 212px; width: 650px;
    display: grid; grid-template-columns: 350px 290px; gap: 0 10px;
    font-family: "Crimson Text", serif; font-size: 20px; line-height: 26px;
    color: var(--white);
  }
  .services ul { list-style: none; }
  .services li { position: relative; padding-left: 22px; }
  .services li::before {
    content: ""; position: absolute; left: 3px; top: 8px;
    width: 10px; height: 10px; border-radius: 50%;
    background: var(--bullet); box-shadow: 0 0 0 1.5px var(--white);
  }
</style>
</head>
<body>
  <section class="card card--front">
    <div class="face">
      <div class="dancer-photo" role="img" aria-label="Dancer in magenta and gold silk costume, hands in a classical pose"></div>
      <h1 class="brand"><span>Copper Lantern</span><span>Indian Dance</span></h1>
      <p class="credentials">
        <span class="name">Tessa Marlowe</span><br>
        Graduate of Kuchipudi<br>
        classical Indian dance
      </p>
      <div class="contact-band">
        <span>T. 0417 862 049</span>
        <span>E. copperlanternindiandance@velmora.com</span>
      </div>
    </div>
  </section>

  <section class="card card--back">
    <div class="face">
      <div class="dancer-photo" role="img" aria-label="Full-length dancer in maroon and gold costume striking a pose"></div>
      <div class="services">
        <ul>
          <li>Indian dance classes +<br>private tuition</li>
          <li>School + preschool educational<br>courses and workshops</li>
          <li>Dance theatre performances</li>
          <li>Community function workshops<br>and performances</li>
        </ul>
        <ul>
          <li>Children's parties</li>
          <li>Wedding + conference<br>performances</li>
          <li>Mouth percussion classes</li>
          <li>Indian mythology and<br>dance demonstration<br>workshops</li>
        </ul>
      </div>
    </div>
  </section>
</body>
</html>
```